Company Proposal Powerpoint Template

We would like to update our overall proposal presentation with a fresh, new look that might appeal to the younger generation. We are a full-meeting management company that specializes in corporate events sales meetings, incentive trips, and tradeshows/conferences.
We have a core set of slides that we use for presentations, but will also need to customize based on the customers we service and what we are selling each potential client.
We have a company logo, but we are not tied into the colors schemes for the logo and are okay adding the logo in black or white versus in color.
I have included our current look and feel for this presentation. This will also give you content that we typically add to this presentation.
Reason: Traveling out of the office so limited access to review the art.
Industry/Entity Type
It Company
Look and feel

```html
<!DOCTYPE html>
<html lang="en">
<head>
<meta charset="utf-8">
<title>MeetWell – Proposal Slide Set</title>
<link href="https://fonts.googleapis.com/css2?family=Roboto+Condensed:wght@300;400;700&display=swap" rel="stylesheet">
<style>
:root{
  --crimson:#d2204a;
  --taupe:#8c857b;
  --charcoal:#4b4845;
  --ink:#3c3c3c;
  --mid:#777;
  --rule:#9a948c;
  --paper:#ffffff;
  --stage:#e6e6e6;
}
*{margin:0;padding:0;box-sizing:border-box}
html,body{width:1200px;height:894px;overflow:hidden;background:var(--stage)}
body{font-family:"Roboto Condensed",Arial,sans-serif;color:var(--ink)}
.deck{position:relative;width:1200px;height:894px;display:grid;
  grid-template-columns:repeat(3,360px);grid-template-rows:repeat(4,203px);
  column-gap:10px;row-gap:9px;padding:29px 0 0 49px}
.slide{position:relative;width:360px;height:203px;background:var(--paper);overflow:hidden}
.abs{position:absolute}
.photo{position:absolute}
.slide-title{position:absolute;left:17px;top:17px;font-size:10px;font-weight:300;color:#666;letter-spacing:.1px}
.title-rule{position:absolute;left:17px;right:17px;top:29px;height:1px;background:#aaa}
.foot-line{position:absolute;left:0;right:0;bottom:0;height:3px;background:var(--rule)}
.foot-tab{position:absolute;right:0;bottom:0;width:80px;height:10px;background:var(--crimson);
  clip-path:polygon(12px 0,100% 0,100% 100%,0 100%);color:#fff;font-size:4px;text-align:right;padding:3px 8px 0 0}
.foot-brand{position:absolute;left:4px;bottom:4px;font-size:5px;color:#777;display:flex;align-items:center;gap:2px}
.foot-brand i{display:block;width:5px;height:5px;border:1px solid var(--crimson)}
.brand{display:flex;align-items:center;gap:4px;color:#555;font-weight:300}
.brand .mark{width:12px;height:12px;border-radius:50%;background:var(--crimson)}
.tiny{font-size:4.3px;line-height:1.45;color:#555}
.white{color:#fff}
.red{color:var(--crimson)}

/* welcome */
.welcome-head{right:20px;top:92px;text-align:right;color:#fff}
.welcome-head h1{font-size:17px;font-weight:400;letter-spacing:.3px}
.welcome-head .sub{font-size:8.5px;letter-spacing:2px;font-weight:300;margin-top:1px}
.welcome-head .date{font-size:5.5px;margin-top:5px;font-weight:700}

/* contents */
.toc-label{left:47px;top:48px;color:#fff;font-weight:300}
.toc-label small{font-size:5px;display:block}
.toc-label strong{font-size:14px;font-weight:300}
.toc-row{position:absolute;left:175px;width:153px;height:11px;display:flex;align-items:center}
.toc-row .num{width:11px;height:11px;border-radius:50%;background:var(--crimson);color:#fff;font-size:5px;
  display:flex;align-items:center;justify-content:center;border:1px solid #fff;position:relative;z-index:1}
.toc-row .bar{flex:1;height:9px;margin-left:-3px;background:#d8d5d0;font-size:5px;color:#555;padding:2px 0 0 14px}

/* vision */
.vm-text{position:absolute;top:168px;width:120px;text-align:center;font-size:5.6px;line-height:1.5;color:#fff;font-weight:300}
.vm-icon{position:absolute;top:115px;width:40px;height:40px;border-radius:50%;background:var(--taupe);border:2px solid #fff}

/* about */
.about-band{left:0;right:0;top:52px;height:66px;background:var(--taupe)}
.about-band p{position:absolute;left:17px;top:20px;font-size:5.6px;line-height:1.5;color:#fff}
.about-list{left:117px;top:132px;font-size:5px;line-height:1.8;color:#444}
.about-list .tick{color:var(--crimson)}

/* team */
.member{position:absolute;width:60px;text-align:center}
.member .pic{width:42px;height:42px;border-radius:50%;border:2px solid var(--crimson);margin:0 auto;
  background:radial-gradient(circle at 50% 40%,#e9c9a6,#b7875a 60%,#7a4a32)}
.member .name{font-size:4.6px;color:var(--crimson);margin-top:2px}
.member .role{font-size:3.6px;color:#777;font-style:italic}

/* services */
.svc-box{position:absolute;padding:6px;color:#fff}
.svc-box h4{font-size:5.4px;font-weight:400;margin-bottom:3px}
.svc-box ul{list-style:none;font-size:3.8px;line-height:1.75}

/* partners */
.partner-frame{left:44px;top:47px;width:290px;height:133px;border:1px solid #ccc;box-shadow:0 3px 4px rgba(0,0,0,.12)}
.partner-grid{position:absolute;left:16px;top:10px;display:grid;grid-template-columns:repeat(4,50px);column-gap:20px;row-gap:16px}
.badge{height:16px;border-radius:2px}

/* charts */
.donut-caption{position:absolute;top:121px;width:80px;text-align:center;font-size:3.8px;line-height:1.5;color:#555}
.chart-copy{left:22px;top:60px;width:160px;font-size:4px;line-height:1.55;color:#444}
.chart-copy b{color:var(--crimson);font-weight:400;display:block}
.chart-copy p{margin-bottom:9px}
.legend{left:240px;top:123px;font-size:3.3px;line-height:1.4;color:#555;width:70px}
.legend div{margin-bottom:6px}
.legend i{display:inline-block;width:4px;height:4px;margin-right:4px;vertical-align:middle}

/* sales */
.sales-band{left:0;right:0;top:136px;bottom:0;background:var(--crimson);color:#fff;padding:20px 20px}
.sales-band h2{font-size:9.5px;font-weight:300;margin-bottom:4px}
.sales-band p{font-size:4.2px;line-height:1.5}

/* image text */
.imgtext{left:0;top:0;width:155px;height:203px;background:var(--taupe);color:#fff;padding:16px 22px}
.imgtext h2{font-size:10px;font-weight:300;margin-bottom:38px}
.imgtext .blk{font-size:3.9px;line-height:1.55;margin-bottom:9px}
.imgtext .blk b{color:var(--crimson);font-weight:400;display:block}

/* thanks */
.thanks-copy{left:28px;top:104px;color:#fff}
.thanks-copy h2{font-size:9.5px;font-weight:700;line-height:1.2}
.thanks-copy h3{font-size:10px;font-weight:300;margin-bottom:14px}
.contact{display:flex;align-items:center;gap:6px;font-size:5.5px;margin-bottom:10px}
.contact .ic{width:8px;height:8px;border-radius:50%;background:#fff;display:flex;align-items:center;justify-content:center}
</style>
</head>
<body>
<main class="deck">

  <!-- 1 welcome -->
  <section class="slide">
    <div class="abs brand" style="left:26px;top:40px;font-size:12px"><span class="mark"></span>MeetWell</div>
    <div class="photo" role="img" aria-label="Silhouettes of a team around a boardroom table against a bright window" style="left:0;top:82px;width:220px;height:76px;background:linear-gradient(90deg,#3b4a6b,#6c7fa3 45%,#b98aa6 80%,#d2204a)"></div>
    <svg class="abs" style="left:0;top:0" width="360" height="203" viewBox="0 0 360 203">
      <path d="M0 82 H120 C150 82 160 62 190 62 H360 V82 H0Z" fill="#fff"/>
      <path d="M200 62 H360 V158 H200 Z" fill="#d2204a"/>
      <path d="M150 158 C170 100 190 62 220 62 L200 62 C170 62 150 82 130 82Z" fill="#fff"/>
      <rect x="0" y="158" width="360" height="2" fill="#d2204a"/>
    </svg>
    <div class="abs welcome-head"><h1>WELCOME</h1><div class="sub">TO OUR PRESENTATION</div><div class="date">Birmingham, March 25, 2016</div></div>
    <div class="abs tiny" style="left:33px;top:176px;font-size:3.4px;line-height:1.3">© 2016 All rights reserved. Contains confidential and proprietary information and may not be disclosed or<br>reproduced without the prior written consent of MeetWell</div>
    <div class="foot-line"></div>
  </section>

  <!-- 2 contents -->
  <section class="slide" style="background:var(--taupe)">
    <div class="photo" role="img" aria-label="Business people gathered around a meeting table, softly faded" style="inset:0;background:linear-gradient(90deg,#a49d93,#8c857b 55%,#9a9389)"></div>
    <div class="abs toc-label"><small>TABLE OF</small><strong>CONTENTS</strong></div>
    <div class="toc-row" style="top:67px"><span class="num">1</span><span class="bar">LOREM IPSUM DOLOR SIT MET</span></div>
    <div class="toc-row" style="top:86px"><span class="num">2</span><span class="bar">LOREM IPSUM DOLOR SIT MET</span></div>
    <div class="toc-row" style="top:104px"><span class="num">3</span><span class="bar">LOREM IPSUM DOLOR SIT MET</span></div>
    <div class="toc-row" style="top:123px"><span class="num">4</span><span class="bar">LOREM IPSUM DOLOR SIT MET</span></div>
    <div class="toc-row" style="top:141px"><span class="num">5</span><span class="bar">LOREM IPSUM DOLOR SIT MET</span></div>
    <div class="toc-row" style="top:160px"><span class="num">6</span><span class="bar">LOREM IPSUM DOLOR SIT MET</span></div>
  </section>

  <!-- 3 vision -->
  <section class="slide" style="background:var(--crimson)">
    <div class="photo" role="img" aria-label="A row of dark light bulbs with one glowing white bulb" style="left:0;top:0;width:360px;height:112px;background:linear-gradient(180deg,#4d4a47,#5e5a56)"></div>
    <div class="abs white" style="left:22px;top:16px;font-size:9px;font-weight:300">VISION &amp; MISSION</div>
    <div class="vm-icon" style="left:75px">
      <svg width="36" height="36" viewBox="0 0 36 36"><g fill="none" stroke="#fff" stroke-width="2.2"><circle cx="12" cy="20" r="5"/><circle cx="24" cy="20" r="5"/><path d="M17 19h2"/></g></svg>
    </div>
    <div class="vm-icon" style="left:225px">
      <svg width="36" height="36" viewBox="0 0 36 36"><g fill="none" stroke="#fff" stroke-width="2"><path d="M9 24a9 9 0 1 1 18 0"/><path d="M18 24l5-6"/></g></svg>
    </div>
    <p class="vm-text" style="left:35px">To provide state of the art logistical and supply chain solutions to the defined needs of our customers using the best people, processes and systems in creating efficient and effective results.</p>
    <p class="vm-text" style="left:185px">To provide state of the art logistical and supply chain solutions to the defined needs of our customers using the best people, processes and systems in creating efficient and effective results.</p>
  </section>

  <!-- 4 about -->
  <section class="slide">
    <div class="slide-title">ABOUT US</div><div class="title-rule"></div>
    <div class="abs about-band"><p>Formed 4 years after MW (1996)<br>as a Direct Response to<br>our Clients' Needs</p></div>
    <div class="photo" role="img" aria-label="Smiling young professionals in white shirts seated in a row" style="left:117px;top:52px;width:243px;height:66px;background:linear-gradient(90deg,#c9b8a6,#ece8e2 50%,#d6d0c8)"></div>
    <div class="abs about-list"><span class="red">One Stop Shopping</span><br>As Former Clients, our mission is to provide what we always wanted:<br><span class="tick">✓</span> Staff with Experience<br><span class="tick">✓</span> Outstanding Value<br><span class="tick">✓</span> The Real Magic - Customized Service</div>
    <div class="foot-brand"><i></i>MeetWell</div><div class="foot-tab">02</div><div class="foot-line"></div>
  </section>

  <!-- 5 team -->
  <section class="slide">
    <div class="slide-title">MEET THE TEAM</div><div class="title-rule"></div>
    <div class="member" style="left:41px;top:53px"><div class="pic" role="img" aria-label="Team member portrait"></div><div class="name">JONATHAN DOE</div><div class="role">President</div></div>
    <div class="member" style="left:156px;top:53px"><div class="pic" role="img" aria-label="Team member portrait"></div><div class="name">JONATHAN DOE</div><div class="role">President</div></div>
    <div class="member" style="left:275px;top:53px"><div class="pic" role="img" aria-label="Team member portrait"></div><div class="name">JONATHAN DOE</div><div class="role">President</div></div>
    <div class="member" style="left:96px;top:110px"><div class="pic" role="img" aria-label="Team member portrait"></div><div class="name">JONATHAN DOE</div><div class="role">President</div></div>
    <div class="member" style="left:221px;top:110px"><div class="pic" role="img" aria-label="Team member portrait"></div><div class="name">JONATHAN DOE</div><div class="role">President</div></div>
    <div class="foot-brand"><i></i>MeetWell</div><div class="foot-tab">02</div><div class="foot-line"></div>
  </section>

  <!-- 6 services -->
  <section class="slide">
    <div class="slide-title">OUR SERVICES</div><div class="title-rule"></div>
    <div class="photo" role="img" aria-label="Corporate meeting room with attendees" style="left:36px;top:59px;width:98px;height:41px;background:linear-gradient(135deg,#8aa3be,#c9d3dd)"></div>
    <div class="svc-box" style="left:134px;top:59px;width:99px;height:61px;background:var(--crimson)"><h4>INCENTIVE PROGRAMS</h4><ul><li>• Sales Incentive Programs</li><li>• Weekend Incentive Programs</li><li>• Incentive Trips</li><li>• Domestic &amp; International</li></ul></div>
    <div class="photo" role="img" aria-label="Crowded conference hall audience" style="left:233px;top:59px;width:97px;height:41px;background:linear-gradient(135deg,#7a3b2c,#c06a4a)"></div>
    <div class="svc-box" style="left:36px;top:100px;width:98px;height:70px;background:var(--taupe)"><h4 style="margin-top:4px">CORPORATE MEETING</h4><ul><li>• Annual Meetings, Sales &amp;</li><li>&nbsp; Marketing Meetings</li><li>• CEO Summits/Board of</li><li>&nbsp; Director's Meetings</li><li>• Investor Meetings / Board Meetings</li><li>• Client &amp; Hospitality Events</li></ul></div>
    <div class="photo" role="img" aria-label="Gala banquet hall with blue stage lighting" style="left:134px;top:120px;width:99px;height:50px;background:linear-gradient(135deg,#1d2a5c,#4d5fa8 60%,#a07ab0)"></div>
    <div class="svc-box" style="left:233px;top:100px;width:97px;height:70px;background:var(--taupe)"><h4 style="margin-top:10px">CONFERENCES &amp; TRADESHOW</h4><ul><li>• Multi-Track Conferences</li><li>• 30 Attendees – 6,000+ Attendees</li><li>• Education &amp; Training</li></ul></div>
    <div class="foot-brand"><i></i>MeetWell</div><div class="foot-tab">02</div><div class="foot-line"></div>
  </section>

  <!-- 7 partners -->
  <section class="slide">
    <div class="slide-title">OUR PARTNERS</div><div class="title-rule"></div>
    <div class="abs partner-frame">
      <div class="partner-grid">
        <div class="badge" style="background:#e0202a"></div><div class="badge" style="background:#2b7a3c"></div><div class="badge" style="background:#1f3a78"></div><div class="badge" style="background:#1c2c4f;width:24px;height:24px;margin-top:-4px"></div>
        <div class="badge" style="background:#3d8fd0"></div><div class="badge" style="background:#222"></div><div class="badge" style="background:#3c7a3a"></div><div class="badge" style="background:#d9232d;width:26px"></div>
        <div class="badge" style="background:#22308a;width:36px"></div><div class="badge" style="background:#e8882c;width:36px"></div><div class="badge" style="background:#2f8a3e"></div><div class="badge" style="background:#e8c845;width:20px;height:20px;border-radius:50%;margin-top:-2px"></div>
        <div class="badge" style="background:#1f3f8c"></div><div class="badge" style="background:#3a4a7a"></div><div class="badge" style="background:#2a3f95"></div><div class="badge" style="background:#3366aa"></div>
      </div>
    </div>
    <div class="foot-brand"><i></i>MeetWell</div><div class="foot-tab">02</div><div class="foot-line"></div>
  </section>

  <!-- 8 chart donuts -->
  <section class="slide">
    <div class="slide-title">OUR CHART</div><div class="title-rule"></div>
    <svg class="abs" style="left:0;top:0" width="360" height="203">
      <g fill="none" stroke-width="5">
        <circle cx="68" cy="87" r="20" stroke="#8c857b"/>
        <circle cx="68" cy="87" r="20" stroke="#d2204a" stroke-dasharray="101.8 125.7" transform="rotate(-90 68 87)"/>
        <circle cx="174" cy="87" r="20" stroke="#8c857b"/>
        <circle cx="174" cy="87" r="20" stroke="#d2204a" stroke-dasharray="35.2 125.7" transform="rotate(-90 174 87) scale(1 -1) translate(0 -174)"/>
        <circle cx="274" cy="87" r="20" stroke="#8c857b"/>
        <circle cx="274" cy="87" r="20" stroke="#d2204a" stroke-dasharray="79.2 125.7" transform="rotate(-90 274 87)"/>
      </g>
      <g fill="#d2204a" font-size="9" font-family="Roboto Condensed, sans-serif" text-anchor="middle" font-weight="700">
        <text x="68" y="90">81%</text><text x="174" y="90">72%</text><text x="274" y="90">63%</text>
      </g>
    </svg>
    <p class="donut-caption" style="left:28px">dolor sit amet, consectetur adipiscing elit, sed do eiusmod tempor incididunt ut labore et dolore magna aliqua. Ut enim ad minim veniam, quis nostrud exercitation ullamco laboris nisi ut aliquip ex ea cosse cillum dolore eu fugiat nulla pariatur.</p>
    <p class="donut-caption" style="left:134px">dolor sit amet, consectetur adipiscing elit, sed do eiusmod tempor incididunt ut labore et dolore magna aliqua. Ut enim ad minim veniam, quis nostrud exercitation ullamco laboris nisi ut aliquip ex ea cosse cillum dolore eu fugiat nulla pariatur.</p>
    <p class="donut-caption" style="left:234px">dolor sit amet, consectetur adipiscing elit, sed do eiusmod tempor incididunt ut labore et dolore magna aliqua. Ut enim ad minim veniam, quis nostrud exercitation ullamco laboris nisi ut aliquip ex ea cosse cillum dolore eu fugiat nulla pariatur.</p>
    <div class="foot-brand"><i></i>MeetWell</div><div class="foot-tab">02</div><div class="foot-line"></div>
  </section>

  <!-- 9 chart bars -->
  <section class="slide">
    <div class="slide-title">OUR CHART</div><div class="title-rule"></div>
    <div class="abs chart-copy">
      <p><b>Lorem ipsum dolor sit amet</b>consectetur adipisicing elit, sed do eiusmod tempor incididunt ut labore et dolore magna aliqua. Ut enim ad minim veniam, quis nostrud exercitation ullamco laboris nisi ut aliquip ex ea commodo consequat. Duis aute irure dolor in reprehenderit in voluptate velit esse cillum dolore eu fugiat nulla pariatur.</p>
      <p><b>Lorem ipsum dolor sit amet</b>consectetur adipisicing elit, sed do eiusmod tempor incididunt ut labore et dolore magna aliqua. Ut enim ad minim veniam, quis nostrud exercitation ullamco laboris nisi ut aliquip ex ea commodo consequat. Duis aute irure dolor in reprehenderit in voluptate velit esse cillum dolore eu.</p>
      <p><b>Lorem ipsum dolor sit amet</b>Excepteur sint occaecat cupidatat non proident, sunt in culpa qui officia deserunt mollit anim id est laborum.Excepteur sint occaecat cupidatat non.</p>
    </div>
    <svg class="abs" style="left:0;top:0" width="360" height="203">
      <line x1="206" y1="42" x2="206" y2="106" stroke="#999" stroke-width=".6"/>
      <line x1="206" y1="106" x2="330" y2="106" stroke="#999" stroke-width=".6"/>
      <g fill="#d2204a"><rect x="210" y="60" width="6" height="46"/><rect x="241" y="73" width="6" height="33"/><rect x="271" y="52" width="6" height="54"/><rect x="300" y="67" width="6" height="39"/></g>
      <g fill="#c8c4bf"><rect x="216" y="87" width="6" height="19"/><rect x="247" y="58" width="6" height="48"/><rect x="277" y="82" width="6" height="24"/><rect x="306" y="80" width="6" height="26"/></g>
      <g fill="#8c857b"><rect x="226" y="81" width="6" height="25"/><rect x="257" y="80" width="6" height="26"/><rect x="286" y="75" width="6" height="31"/><rect x="316" y="55" width="6" height="51"/></g>
      <g font-size="4" fill="#666" font-family="Roboto Condensed, sans-serif" text-anchor="middle"><text x="220" y="112">2009</text><text x="251" y="112">2010</text><text x="281" y="112">2011</text><text x="311" y="112">2012</text></g>
    </svg>
    <div class="abs legend">
      <div><i style="background:var(--crimson)"></i>LOREM IPSUM<br>Lorem ipsum dolor sit amet consectetur adipiscing elit sed do eiusmod tempor incididunt ut labore et dolore magna</div>
      <div><i style="background:#c8c4bf"></i>LOREM IPSUM<br>Lorem ipsum dolor sit amet consectetur adipiscing elit sed do eiusmod tempor incididunt ut labore et dolore magna</div>
      <div><i style="background:var(--taupe)"></i>LOREM IPSUM</div>
    </div>
    <div class="foot-brand"><i></i>MeetWell</div><div class="foot-tab">02</div><div class="foot-line"></div>
  </section>

  <!-- 10 sales meeting -->
  <section class="slide">
    <div class="photo" role="img" aria-label="Large audience seated in a red auditorium facing a stage" style="left:0;top:0;width:360px;height:136px;background:linear-gradient(180deg,#3a2620,#7a3a2e 45%,#a4554a)"></div>
    <div class="abs sales-band"><h2>SALES MEETING &amp; CONFERENCE</h2><p>consectetur adipisicing elit, sed do eiusmod tempor incididunt ut labore et dolore magna aliqua.<br>Ut enim ad minim veniam, quis nostrud exercitation ullamco laboris nisi ut aliquip ex ea commodo consequat.</p></div>
  </section>

  <!-- 11 image text -->
  <section class="slide">
    <div class="abs imgtext">
      <h2>IMAGE TEXT</h2>
      <div class="blk"><b>One Stop Shopping</b>With a master contract already in place, MWG can provide Northwind Foods with a full scope of meeting management services options; we become an extension of your team</div>
      <div class="blk"><b>Global Experience</b>Average experience on our team of 19+ years</div>
      <div class="blk"><b>Unparalleled Value</b>Flat fee pricing model and transparent pass-through costs – no surprises!<br>Outstanding Customized Service<br>93% retention rate</div>
    </div>
    <div class="photo" role="img" aria-label="Black and white portrait of a smiling young business team" style="left:155px;top:0;width:205px;height:203px;background:linear-gradient(90deg,#e8e8e8,#9a9a9a 50%,#d0d0d0)"></div>
    <div class="abs" style="left:3px;bottom:4px;width:36px;height:9px;background:#fff;font-size:4.5px;color:#777;padding:2px 3px">MeetWell</div>
  </section>

  <!-- 12 thank you -->
  <section class="slide">
    <div class="abs brand" style="left:20px;top:42px;font-size:12px"><span class="mark"></span>MeetWell</div>
    <svg class="abs" style="left:0;top:0" width="360" height="203">
      <path d="M0 82 H150 C175 82 180 62 205 62 H360 V203 H0Z" fill="#d2204a"/>
    </svg>
    <div class="abs thanks-copy">
      <h2>THANK YOU</h2><h3>FOR YOUR TIME</h3>
      <div class="contact"><span class="ic"><svg width="6" height="6" viewBox="0 0 6 6"><path d="M3 .8 .8 3H1.5V5.2H4.5V3H5.2Z" fill="#d2204a"/></svg></span>4120 Harbor Lane Ste 300</div>
      <div class="contact"><span class="ic"><svg width="6" height="6" viewBox="0 0 6 6"><rect x=".8" y="1.5" width="4.4" height="3" fill="none" stroke="#d2204a" stroke-width=".7"/><path d="M.8 1.5 3 3.3 5.2 1.5" fill="none" stroke="#d2204a" stroke-width=".6"/></svg></span>hello@meetwell.example</div>
      <div class="contact"><span class="ic"><svg width="6" height="6" viewBox="0 0 6 6"><circle cx="3" cy="3" r="1.8" fill="none" stroke="#d2204a" stroke-width=".7"/></svg></span>www.meetwell.example</div>
    </div>
    <div class="photo" role="img" aria-label="Street map showing the office location" style="left:223px;top:71px;width:110px;height:110px;border-radius:50%;background:radial-gradient(circle at 40% 40%,#f4f2ee,#dcd8d0);border:2px solid #fff"></div>
    <svg class="abs" style="left:277px;top:99px" width="10" height="14" viewBox="0 0 10 14"><path d="M5 13C5 13 1 7.5 1 5a4 4 0 0 1 8 0C9 7.5 5 13 5 13Z" fill="#d2204a"/><circle cx="5" cy="5" r="1.5" fill="#fff"/></svg>
  </section>

</main>
</body>
</html>
```